Adventurous female pilot

I am looking for a personal business card, for a very well qualified female pilot, with a lot of aviation experience.

Currently an airline pilot, have worked as a bush pilot in Africa, looking to get into corporate aviation, or private jet owners.
Want a classy looking card for networking...

Could be interested in a retro\vintage look also?!

An idea,, is an african sunset background, with my wings\logo on it
Updates

I just want to say thank you to all of your for your amazing designs!

I have been very busy flying this past week , so not had a chance to be on the computer much.
But I provide some feedback, and conclusions very soon!
Thank you again.

Marla

Reason: Still waiting on a couple of revisions to be 100% about my choice!

Target Market(s)

corporate aviation, private jet owners, casino's,
General audience.
networking

Industry/Entity Type

Airline

Requirements
Nice to have
• Classy, edgy, sexy, but also feminine

```html
<!DOCTYPE html>
<html lang="en">
<head>
<meta charset="utf-8">
<title>Marla Keller – Business Card</title>
<link rel="stylesheet" href="https://fonts.googleapis.com/css2?family=Bebas+Neue&family=Open+Sans:wght@400&display=swap">
<style>
  :root {
    --ink: #1d1d1d;
    --lime: #b6ff00;
    --paper: #ffffff;
    --slate: #3e4a4c;
    --mist: #d9e2e3;
  }
  html, body {
    margin: 0;
    width: 1200px;
    height: 1000px;
    overflow: hidden;
    background: var(--paper);
  }
  .card {
    position: relative;
    width: 1200px;
    height: 1000px;
  }
  .card-frame {
    position: absolute;
    inset: 0;
  }
  .frame-dark { fill: var(--ink); }
  .frame-accent { fill: var(--lime); }
  .card-face { fill: var(--paper); }
  .brand-mark { fill: var(--mist); }

  .brand-name {
    position: absolute;
    left: 400px;
    top: 553px;
    width: 400px;
    text-align: center;
    font-family: "Open Sans", sans-serif;
    font-weight: 400;
    color: var(--slate);
    margin: 0;
    letter-spacing: 0.5px;
  }
  .brand-name span { display: block; }
  .brand-line-main { font-size: 27px; line-height: 32px; }
  .brand-line-sub { font-size: 22px; line-height: 26px; }

  .contact {
    position: absolute;
    left: 795px;
    top: 552px;
    color: var(--ink);
  }
  .contact-name {
    font-family: "Bebas Neue", sans-serif;
    font-weight: 400;
    font-size: 64px;
    line-height: 1;
    margin: 0;
  }
  .contact-role {
    font-family: "Open Sans", sans-serif;
    font-size: 20px;
    line-height: 26px;
    margin: 0 0 1px;
  }
  .contact-list {
    list-style: none;
    padding: 0;
    margin: 0;
    font-family: "Open Sans", sans-serif;
    font-size: 21px;
  }
  .contact-list li {
    display: flex;
    align-items: center;
    height: 41.5px;
    white-space: nowrap;
  }
  .contact-icon {
    width: 22px;
    height: 22px;
    margin-right: 16px;
    flex: none;
  }
  .contact-icon .solid { fill: var(--ink); }
  .contact-icon .outline { fill: none; stroke: var(--ink); stroke-width: 1.4; }
</style>
</head>
<body>
<main class="card">
  <svg class="card-frame" width="1200" height="1000" viewBox="0 0 1200 1000" aria-hidden="true">
    <polygon class="frame-dark" points="37,164 898,164 954,220 93,220 93,631 37,575"/>
    <polygon class="frame-accent" points="916,164 1162,164 1162,410 1106,354 1106,220 972,220"/>
    <polygon class="frame-dark" points="1162,428 1162,839 302,839 246,783 1106,783 1106,372"/>
    <polygon class="frame-accent" points="37,593 93,649 93,783 228,783 284,839 37,839"/>
    <rect class="card-face" x="93" y="220" width="1013" height="563"/>
    <circle class="brand-mark" cx="597" cy="443" r="62"/>
  </svg>

  <p class="brand-name"><span class="brand-line-main">MARLA KELLER</span><span class="brand-line-sub">AVIATION</span></p>

  <section class="contact">
    <h1 class="contact-name">MARLA KELLER</h1>
    <p class="contact-role">Airline Pilot</p>
    <ul class="contact-list">
      <li>
        <svg class="contact-icon" viewBox="0 0 24 24"><path class="solid" d="M6.6 10.8c1.4 2.8 3.8 5.1 6.6 6.6l2.2-2.2c.3-.3.7-.4 1-.2 1.1.4 2.3.6 3.6.6.6 0 1 .4 1 1V20c0 .6-.4 1-1 1C10.6 21 3 13.4 3 4c0-.6.4-1 1-1h3.5c.6 0 1 .4 1 1 0 1.3.2 2.5.6 3.6.1.3 0 .7-.2 1L6.6 10.8z"/></svg>
        +1 702-555-0148
      </li>
      <li>
        <svg class="contact-icon" viewBox="0 0 24 24"><path class="solid" d="M6.6 10.8c1.4 2.8 3.8 5.1 6.6 6.6l2.2-2.2c.3-.3.7-.4 1-.2 1.1.4 2.3.6 3.6.6.6 0 1 .4 1 1V20c0 .6-.4 1-1 1C10.6 21 3 13.4 3 4c0-.6.4-1 1-1h3.5c.6 0 1 .4 1 1 0 1.3.2 2.5.6 3.6.1.3 0 .7-.2 1L6.6 10.8z"/></svg>
        +886 900-555-120
      </li>
      <li>
        <svg class="contact-icon" viewBox="0 0 22 22"><rect class="outline" x="1.5" y="5" width="19" height="13"/><path class="outline" d="M1.5 5l9.5 8 9.5-8M1.5 18l7-6.5M20.5 18l-7-6.5"/></svg>
        marlakeller@mail.com
      </li>
    </ul>
  </section>
</main>
</body>
</html>
```